PEACFUL ACUPUNCTURE PRACTITIONER NEEDS A NEW COAT

I need a new design for an exiting website http://willowgateneedlework.com/ for a acupuncturist. This will be a minimalism design with lots and lots of white space. Home page and one interior page. Please keep the feeling of calm and peaceful serenity. For Color scheme: https://www.morningfernclinic.com/fertility. The bottom part of the home page with sections and links to the service pages: https://harborlotuswellness.com/. The client likes this the best: http://mfclinic.com/. I'm attaching the logo and content pages.

Target Market(s)

Women

Industry/Entity Type

Wellness, health, wellbeing, meditation

Number of Pages Required

2 page

Font styles to use
Sans Serif
Decorative

Colors

Designer to choose colors to be used in the design.

Requirements
Must have
Nice to have
• Follow new website drafts and links
Should not have
• Busy with bright colors. No poping

```html
<!DOCTYPE html>
<html lang="en">
<head>
<meta charset="utf-8">
<title>Willowgate Acupuncture</title>
<link href="https://fonts.googleapis.com/css2?family=Lora:wght@400;500&family=Roboto:wght@400;500;700&display=swap" rel="stylesheet">
<style>
:root{
  --rose:#c08a8e;
  --rose-light:#d6b0b3;
  --rose-pale:#e8cfd1;
  --ink:#1e1e1e;
  --text:#555;
  --mist:#f3f2f2;
  --footer:#2f2e2e;
  --white:#fff;
}
*{box-sizing:border-box;margin:0;padding:0}
html,body{width:1200px;height:3953px;overflow:hidden}
body{position:relative;font-family:'Roboto',sans-serif;color:var(--text);background:var(--white)}
.abs{position:absolute}
.serif{font-family:'Lora',serif;font-weight:400;color:var(--ink)}
.btn{display:flex;align-items:center;justify-content:space-between;height:50px;border-radius:25px;background:var(--rose);color:var(--white);font-weight:700;font-size:14px;letter-spacing:.3px;padding:0 6px 0 30px}
.btn .dot{width:38px;height:38px;border-radius:50%;background:var(--white);display:flex;align-items:center;justify-content:center}
.btn .dot span{width:22px;height:22px;border-radius:50%;border:2px solid var(--rose-light)}
/* header */
.topbar{top:0;left:0;width:1200px;height:100px}
.contact-item{display:flex;align-items:center;gap:16px}
.circle-icon{width:34px;height:34px;border-radius:50%;background:var(--rose-light);display:flex;align-items:center;justify-content:center}
.contact-label{font-size:11px;font-weight:700;color:var(--ink);text-transform:uppercase}
.contact-value{font-size:12px;color:#444;margin-top:3px}
.phone-big{font-size:26px;font-weight:700;color:var(--rose-light);margin-top:2px}
.brand{left:0;width:1200px;top:22px;text-align:center}
.brand-mark{width:36px;height:36px;border-radius:50%;background:var(--rose-light);margin:0 auto 4px}
.brand-name{font-family:'Lora',serif;font-size:21px;color:#666}
.nav{top:100px;left:0;width:1200px;height:47px;background:var(--rose)}
.nav ul{list-style:none;display:flex;gap:30px;position:absolute;left:111px;top:0;height:47px;align-items:center}
.nav li{color:var(--white);font-size:13px;font-weight:700}
.nav .cta{position:absolute;left:904px;top:0;width:184px;height:47px;background:var(--rose-pale);color:var(--white);font-size:14px;font-weight:700;display:flex;align-items:center;justify-content:center}
/* hero */
.hero{top:147px;left:0;width:1200px;height:561px;background:linear-gradient(100deg,#8d8685 0%,#a59a97 35%,#c7a596 60%,#d9b09a 100%)}
.hero h1{position:absolute;left:109px;top:150px;font-size:58px;color:var(--white)}
.hero p{position:absolute;left:110px;top:240px;width:540px;font-size:13.5px;line-height:24px;color:var(--white)}
.hero .btn{position:absolute;left:110px;top:348px;width:180px}
.arrow{position:absolute;top:265px}
/* about */
.about-band{top:832px;left:0;width:408px;height:454px;background:var(--rose)}
.about-vertical{left:120px;top:1212px;transform:rotate(-90deg);transform-origin:0 0;font-family:'Lora',serif;font-size:58px;color:rgba(255,255,255,.32);white-space:nowrap}
.about-photo{left:256px;top:872px;width:311px;height:371px;border:6px solid var(--rose);border-radius:8px;background:linear-gradient(160deg,#efe8e2,#d8c6bb 60%,#b99e8d)}
.about-text{left:650px;top:890px;width:426px}
.about-text h2{font-size:44px;margin-bottom:22px}
.about-text p{font-size:13.5px;line-height:26.5px}
.about-text .btn{width:184px;margin-top:16px}
/* areas */
.areas{top:1414px;left:0;width:1200px;height:473px;background:var(--mist)}
.areas h2{position:absolute;top:76px;left:0;width:1200px;text-align:center;font-size:44px}
.focus-card{position:absolute;top:180px;width:235px;height:207px;border:2px solid var(--rose-light);border-radius:6px;background:#f5f5f5;text-align:center}
.focus-card .icon{width:64px;height:64px;margin:24px auto 26px;border-radius:50%;background:var(--rose)}
.focus-card h3{font-size:17px;font-weight:700;color:var(--ink);line-height:24px}
/* treatments */
.treat-title{top:1973px;left:0;width:1200px;text-align:center;font-size:44px}
.treat-text{width:430px}
.treat-text h3{font-family:'Lora',serif;font-weight:400;font-size:27px;color:var(--ink);margin-bottom:18px}
.treat-text p{font-size:13.5px;line-height:25px;text-align:justify}
.treat-text .btn{width:184px;margin-top:22px}
.treat-photo{width:449px;height:321px}
.treat-photo .pic{position:absolute;inset:0 0 0 6px}
.treat-photo .strip{position:absolute;left:0;top:0;width:6px;height:100%;background:var(--rose)}
.treat-photo.right-strip .pic{inset:0 0 0 0}
.badge{width:72px;height:72px;border-radius:50%;background:var(--rose);border:5px solid var(--white);box-shadow:0 0 0 1px var(--rose-light)}
/* cta */
.cta-band{top:3294px;left:0;width:1200px;height:290px;background:var(--rose);text-align:center;color:var(--white)}
.cta-band h2{font-family:'Lora',serif;font-weight:400;font-size:46px;margin-top:68px}
.cta-band h4{font-size:16px;font-weight:700;margin-top:22px}
.cta-band p{font-size:16px;line-height:29px;margin-top:22px}
.cta-band b{font-size:20px}
/* footer */
.footer{top:3584px;left:0;width:1200px;height:369px;background:var(--footer);color:var(--white)}
.footer h5{position:absolute;top:73px;font-size:13px;font-weight:700;letter-spacing:.3px}
.foot-contact{position:absolute;left:110px;display:flex;align-items:center;gap:20px;font-size:12px;line-height:18px}
.foot-contact .ring{width:34px;height:34px;border-radius:50%;border:1px solid #777;display:flex;align-items:center;justify-content:center}
.foot-list{position:absolute;list-style:none;font-size:12.5px}
.foot-list li{height:34.5px;display:flex;gap:14px}
.foot-list li::before{content:"»";font-weight:700}
.socials{position:absolute;left:557px;top:228px;display:flex;gap:8px}
.socials span{width:34px;height:34px;border-radius:50%;border:1px solid #999}
.field{position:absolute;height:37px;border:1px solid #777;border-radius:3px;background:var(--footer);font-size:11.5px;padding:10px 16px}
.submit{position:absolute;left:781px;top:274px;width:126px;height:40px;border-radius:20px;background:var(--rose-light);font-size:13px;font-weight:700;display:flex;align-items:center;justify-content:center}
.foot-rule{position:absolute;left:110px;top:354px;width:980px;height:1px;background:#777}
</style>
</head>
<body>

<header class="abs topbar">
  <div class="abs contact-item" style="left:110px;top:29px">
    <div class="circle-icon"><svg width="14" height="11" viewBox="0 0 14 11"><rect x="0.5" y="0.5" width="13" height="10" rx="1" fill="none" stroke="#fff"/><path d="M1 1l6 5 6-5" fill="none" stroke="#fff"/></svg></div>
    <div><div class="contact-label">Email us</div><div class="contact-value">maren@willowgateneedlework.com</div></div>
  </div>
  <div class="abs brand">
    <div class="brand-mark"></div>
    <div class="brand-name">Willowgate Acupuncture</div>
  </div>
  <div class="abs contact-item" style="left:870px;top:26px">
    <div class="circle-icon"><svg width="14" height="14" viewBox="0 0 24 24"><path fill="#fff" d="M6.6 10.8a15 15 0 006.6 6.6l2.2-2.2a1 1 0 011-.25 11 11 0 003.6.6 1 1 0 011 1V20a1 1 0 01-1 1A17 17 0 013 4a1 1 0 011-1h3.5a1 1 0 011 1 11 11 0 00.6 3.6 1 1 0 01-.25 1z"/></svg></div>
    <div><div class="contact-label">Free 30 minute consult</div><div class="phone-big">413-555-0147</div></div>
  </div>
</header>

<nav class="abs nav">
  <ul><li>HOME</li><li>ABOUT MAREN</li><li>TREATMENTS</li><li>HEALTH CONCERNS</li><li>FERTILITY</li><li>PREGNANCY</li><li>CONTACT</li></ul>
  <div class="cta">SCHEDULE NOW</div>
</nav>

<section class="abs hero" role="img" aria-label="Photo of acupuncture needles placed along a woman's back">
  <svg class="arrow" style="left:46px" width="18" height="30" viewBox="0 0 18 30"><path d="M15 3L3 15l12 12" fill="none" stroke="#fff" stroke-width="3"/></svg>
  <svg class="arrow" style="left:1136px" width="18" height="30" viewBox="0 0 18 30"><path d="M3 3l12 12L3 27" fill="none" stroke="#fff" stroke-width="3"/></svg>
  <h1 class="serif" style="color:#fff">Philosophy of Care</h1>
  <p>Acupuncture &amp; Chinese Herbal Medicine are rooted in over 3000 years of history &amp; tradition. As a complete medical system that has remained flexible &amp; relevant we honor what has workedfrom the past while embracing the medicine of tomorrow.</p>
  <div class="btn"><span>GET STARTED</span><span class="dot"><span></span></span></div>
</section>

<div class="abs about-band"></div>
<div class="abs about-vertical">About Maren</div>
<div class="abs about-photo" role="img" aria-label="Portrait photo of the acupuncturist"></div>
<section class="abs about-text">
  <h2 class="serif">About Maren</h2>
  <p>Maren Holloway is a Massachusetts and California Licensed Acupuncturist and Herbalist as well as Nationally Certified in both Acupuncture and Herbal Medicine. She obtained her Masters Degree from Stillwater University in Santa Cruz CA and has studied at the integrated hospital in Hang Zhou China. She has also done extensive study in Chi Nei Tsang in both the USA and Thailand. She worked for Linden Herb Company a leader of high quality, lab tested</p>
  <div class="btn"><span>LEARN MORE</span><span class="dot"><span></span></span></div>
</section>

<section class="abs areas">
  <h2 class="serif">Areas of focus</h2>
  <div class="focus-card" style="left:108px"><div class="icon"></div><h3>FERTILITY<br>&amp; PREGNANCY</h3></div>
  <div class="focus-card" style="left:358px"><div class="icon"></div><h3>EMOTIONAL WELL<br>BEING</h3></div>
  <div class="focus-card" style="left:608px"><div class="icon"></div><h3>HORMONE<br>BALANCE</h3></div>
  <div class="focus-card" style="left:858px"><div class="icon"></div><h3>STRENGTH<br>&amp; STRUCTURE</h3></div>
</section>

<h2 class="abs serif treat-title">Our Treatments</h2>

<section class="abs treat-text" style="left:117px;top:2093px">
  <h3>ACUPUNCTURE TREATMENTS</h3>
  <p>Acupuncture uses the insertion of thin needles at specific points to act as guideposts for healing. These guideposts help the body use its own mechanisms for self regulation to restore health.The needles used are sterile, disposable and as thin as a cat's whisker. Often they create a slight tingling sensation at individual points but rarely is there pain or discomfort. After the acupuncture needles are placed, a period of rest allows</p>
  <div class="btn"><span>LEARN MORE</span><span class="dot"><span></span></span></div>
</section>
<div class="abs treat-photo" style="left:634px;top:2082px">
  <div class="strip"></div>
  <div class="pic" role="img" aria-label="Photo of acupuncture needles in a shoulder" style="background:linear-gradient(150deg,#5c4d48,#b88f7d 45%,#d3a993)"></div>
</div>
<div class="abs badge" style="left:609px;top:2207px"></div>

<div class="abs treat-photo right-strip" style="left:110px;top:2471px">
  <div class="pic" role="img" aria-label="Photo of dried Chinese herbs arranged on a tray" style="background:linear-gradient(135deg,#c9b49a,#e2d2b8 45%,#8f4f3e)"></div>
  <div class="strip" style="left:auto;right:-6px"></div>
</div>
<div class="abs badge" style="left:510px;top:2595px"></div>
<section class="abs treat-text" style="left:640px;top:2482px">
  <h3>HERBAL FORMULAS</h3>
  <p style="text-align:left">Herbal formulas aid in extending and enhancing acupuncture treatments. Daily use acts as a reinforcing agent, encouraging the body towards a healthier path until it is strong enough to take over on its own. Herbs rarely have side effects and can be taken as a tea, tablet or tincture. All herbal formulas used at Willowgate Acupuncture have passed stringent lab analysis within the United States as well as China. This guarantees not only the proper</p>
  <div class="btn"><span>LEARN MORE</span><span class="dot"><span></span></span></div>
</section>

<section class="abs treat-text" style="left:117px;top:2873px">
  <h3>ABDOMINAL MASSAGE</h3>
  <p style="text-align:left">The center of the body has a strong tendency to subconsciously store tension and emotional frustration. This tension accumulates over time limiting blood flow and creating stagnation. Abdominal massage works to unwind these accumulated adhesions allowing for better digestion, easier menstrual cycles, increased fertility and improved coping mechanisms for stress through deeper breathing.</p>
  <div class="btn"><span>LEARN MORE</span><span class="dot"><span></span></span></div>
</section>
<div class="abs treat-photo" style="left:634px;top:2861px">
  <div class="strip"></div>
  <div class="pic" role="img" aria-label="Photo of hands forming a heart around a navel" style="background:linear-gradient(160deg,#c98f74,#e6bca4 50%,#d69e84)"></div>
</div>
<div class="abs badge" style="left:609px;top:2987px"></div>

<section class="abs cta-band">
  <h2>Acupuncture Can Help!</h2>
  <h4>SCHEDULE A FREE 30 MINUTE CONSULTATION</h4>
  <p>Consultations are always available to help answer any questions you may have about acupuncture<br>or herbal medicine in a relaxed environment. <b>413-555-0147</b></p>
</section>

<footer class="abs footer">
  <h5 style="left:110px">QUICK LINKS</h5>
  <div class="foot-contact" style="top:118px"><div class="ring"><svg width="12" height="14" viewBox="0 0 12 14"><path d="M6 13S1 8 1 5a5 5 0 0110 0c0 3-5 8-5 8z" fill="none" stroke="#aaa"/><circle cx="6" cy="5" r="1.6" fill="#aaa"/></svg></div><div>14 Alder Row<br>Easthollow, MA 01099</div></div>
  <div class="foot-contact" style="top:172px"><div class="ring"><svg width="13" height="13" viewBox="0 0 24 24"><path fill="#aaa" d="M6.6 10.8a15 15 0 006.6 6.6l2.2-2.2a1 1 0 011-.25 11 11 0 003.6.6 1 1 0 011 1V20a1 1 0 01-1 1A17 17 0 013 4a1 1 0 011-1h3.5a1 1 0 011 1 11 11 0 00.6 3.6 1 1 0 01-.25 1z"/></svg></div><div style="font-size:17px;font-weight:700">413-555-0147</div></div>
  <div class="foot-contact" style="top:225px"><div class="ring"><svg width="13" height="10" viewBox="0 0 14 11"><rect x="0.5" y="0.5" width="13" height="10" rx="1" fill="none" stroke="#aaa"/><path d="M1 1l6 5 6-5" fill="none" stroke="#aaa"/></svg></div><div>maren@willowgateneedlework.com</div></div>

  <h5 style="left:412px">QUICK LINKS</h5>
  <ul class="foot-list" style="left:412px;top:113px"><li>Home</li><li>About Us</li><li>Treatments</li><li>Reviews</li><li>Contact us</li></ul>

  <h5 style="left:557px">WORKING HOURS</h5>
  <ul class="foot-list" style="left:557px;top:113px"><li>Tue - Fri &nbsp;: &nbsp;10.00 - 06.00</li><li>Saturday &nbsp;: &nbsp;10.00 - 03.00</li><li>Sunday &nbsp; : &nbsp;Closed</li></ul>
  <div class="socials"><span></span><span></span><span></span><span></span></div>

  <h5 style="left:781px">SUBSCRIBE TO OUR MAILING LIST</h5>
  <div class="field" style="left:781px;top:107px;width:149px">Name</div>
  <div class="field" style="left:938px;top:107px;width:150px">Email</div>
  <div class="field" style="left:781px;top:154px;width:307px">Phone No</div>
  <div class="field" style="left:781px;top:200px;width:307px;height:58px">Location</div>
  <div class="submit">SUBMIT</div>
  <div class="foot-rule"></div>
</footer>

</body>
</html>
```